Pain Management, Personal Injury & Motor Vehicle Accident

I need t rack card to use as marketing collateral while talking to urgent cares, wreckers services, primary care, and emergency room staff
If you have been involved in a motor vehicle accident or personal injury accident, Prairie Ridge Relief Clinic is your Solution to complete pain relief. We understand your pain and are here to assist you along the journey to becoming pain free. It is crucial that you choose a physician who is experienced in treating your unique injury.
At Prairie Ridge Relief Clinic, Dr Colin Marsh and his team of experts will provide you with a specialized approach to reducing and managing your pain with a comprehensive and effective treatment plan based on a proper diagnosis. You can expect an exceptional treatment program for your injuries to help you to begin improving your quality of life immediately.
We treat:
Car Accident Injuries
Semi Truck Injuries
Most Personal Injuries
Slip and Falls
Motorcycle Accident Injuries
Whiplash
Back Injuries
Neck Injuries
Shoulder Injuries
Headaches
Locations: Cedar Bend, Hollis Park, Linwood
Phone: (580) 472-6193
Fax: (833) 718-2947
www.prairieridgerelief.example
Target Market(s)
Urgent Cares, Emergency Rooms, Primary Care, Wrecker Services, anyone involved in a Personal Injury or Motor Vehicle Accident
Industry/Entity Type
Healthcare, Motor Vehicle Accident Injury, Personal Injury, Pain Management, Pain Relief

```html
<!DOCTYPE html>
<html lang="en">
<head>
<meta charset="utf-8">
<title>Prairie Ridge Relief Clinic – Rack Card</title>
<link href="https://fonts.googleapis.com/css2?family=Roboto:wght@400;500;700&family=Roboto+Slab:wght@400;700;800&display=swap" rel="stylesheet">
<style>
  :root{
    --red:#d3141c;
    --red-dark:#a70d12;
    --ink:#2a2a2a;
    --black:#0d0d0d;
    --white:#ffffff;
    --mist:#eeeeee;
    --grey:#cfcfcf;
    --stage:#d6d6d6;
  }
  *{margin:0;padding:0;box-sizing:border-box}
  html,body{width:689px;height:1200px;overflow:hidden}
  body{background:var(--stage);font-family:"Roboto",sans-serif;position:relative}

  .card{position:absolute;top:240px;width:320px;height:720px;background:var(--white);overflow:hidden;
        box-shadow:0 2px 8px rgba(0,0,0,.18)}
  .card--front{left:16px}
  .card--back{left:353px}

  .card__stripes{position:absolute;top:0;left:0;right:0;height:6px;
        background:linear-gradient(var(--red) 0 3px,var(--ink) 3px 6px)}
  .card__backdrop{position:absolute;top:6px;left:0;right:0;height:420px;
        background:linear-gradient(180deg,var(--white) 0%,var(--mist) 55%,var(--white) 100%)}

  .brand{position:absolute;top:50px;left:0;right:0;display:flex;align-items:center;justify-content:center;gap:8px}
  .brand__dot{width:10px;height:10px;border-radius:50%;background:var(--red);flex:none}
  .brand__text{font-family:"Roboto Slab",serif;font-weight:400;color:var(--ink);font-size:9.5px;line-height:12px}
  .brand__name{font-size:11.5px;line-height:14px}

  .front__photo{position:absolute;top:92px;left:0}

  .headline{position:absolute;top:405px;left:0;right:0;text-align:center;font-family:"Roboto Slab",serif;font-weight:800;line-height:28px}
  .headline__lead{display:block;font-size:25px;color:var(--ink)}
  .headline__accent{display:block;font-size:25px;color:var(--red)}
  .audience{position:absolute;top:466px;left:0;right:0;text-align:center;font-family:"Roboto Slab",serif;
        font-size:9.5px;line-height:12.5px;color:var(--ink)}
  .copy{position:absolute;left:21px;right:21px;font-size:8.3px;line-height:10.6px;color:var(--ink);text-align:justify}
  .copy--intro{top:506px}
  .copy--team{top:577px}

  .front__footer{position:absolute;left:0;right:0;bottom:0;height:70px;background:var(--black);color:var(--white)}
  .contact{position:absolute;display:flex;align-items:center;gap:6px}
  .contact--area{left:21px;top:13px;font-size:8.5px;font-weight:700;line-height:10px}
  .contact--fax{left:21px;top:42px;font-size:12.5px;font-weight:700}
  .contact--phone{left:183px;top:14px;height:20px;padding:0 10px 0 5px;border-radius:10px;background:var(--red);
        font-size:11.5px;font-weight:500}
  .contact--web{left:183px;top:44px;font-size:7px}
  .contact--web em{font-style:normal;color:var(--red)}
  .icon{flex:none;display:block}

  .back__gallery{position:absolute;top:130px;left:0}
  .back__panel{position:absolute;top:0;left:0}
  .conditions{position:absolute;top:458px;left:0;right:0;text-align:center;color:var(--white)}
  .conditions__kicker{display:block;font-family:"Roboto",sans-serif;font-weight:500;font-size:18px;letter-spacing:.3px;line-height:20px}
  .conditions__title{display:block;font-family:"Roboto Slab",serif;font-weight:800;font-size:37px;line-height:40px}
  .conditions__list{position:absolute;top:534px;list-style:none;color:var(--white);font-size:9.8px;font-weight:500}
  .conditions__list--left{left:23px}
  .conditions__list--right{left:196px}
  .conditions__list li{display:flex;align-items:center;gap:5px;height:16.5px}
  .back__web{position:absolute;top:635px;left:102px;display:flex;align-items:center;gap:4px;color:var(--white);font-size:7px}
  .back__base{position:absolute;left:0;right:0;bottom:0;height:64px;background:var(--white)}
  .portrait{position:absolute;top:624px;width:60px;height:60px}
  .portrait--physician{left:40px}
  .portrait--nurse{left:216px}
  .staff{position:absolute;top:690px;text-align:center;font-family:"Roboto Slab",serif;font-size:7px;line-height:9.5px;color:var(--ink)}
  .staff--physician{left:18px;width:110px}
  .staff--nurse{left:190px;width:118px}
</style>
</head>
<body>

<section class="card card--front">
  <div class="card__backdrop"></div>
  <div class="card__stripes"></div>

  <div class="brand">
    <span class="brand__dot"></span>
    <p class="brand__text">Marsh Medical, LLC dba<br><span class="brand__name">Prairie Ridge Relief Clinic</span><br>Dr. Colin E. Marsh, MD</p>
  </div>

  <svg class="front__photo" width="320" height="320" viewBox="0 0 320 320">
    <defs>
      <linearGradient id="parkTones" x1="0" y1="0" x2="1" y2="1">
        <stop offset="0" stop-color="#5f7a3c"/>
        <stop offset=".5" stop-color="#8aa05a"/>
        <stop offset="1" stop-color="#a79c82"/>
      </linearGradient>
    </defs>
    <path role="img" aria-label="Photo: a smiling couple holding hands on a leafy park path"
          d="M0,30 C90,-5 210,30 320,10 L320,262 C230,300 120,325 0,245 Z" fill="url(#parkTones)"/>
    <path d="M0,236 C90,270 160,270 210,258 C250,248 290,238 320,240 L320,262 C260,270 210,300 150,302 C90,304 40,280 0,248 Z"
          fill="var(--red)"/>
  </svg>

  <h1 class="headline">
    <span class="headline__lead">Relieving Pain,</span>
    <span class="headline__accent">Improving Lives</span>
  </h1>
  <p class="audience">Urgent cares, wreckers services, primary care,<br>and emergency room staff</p>

  <p class="copy copy--intro">If you have been involved in a motor vehicle accident or personal injury accident, Prairie Ridge Relief Clinic is your Solution to complete pain relief. We understand your pain and are here to assist you along the journey to becoming pain free. It is crucial that you choose a physician who is experienced in treating your unique injury.</p>
  <p class="copy copy--team">At Prairie Ridge Relief Clinic, Dr Colin Marsh and his team of experts will provide you with a specialized approach to reducing and managing your pain with a comprehensive and effective treatment plan based on a proper diagnosis. You can expect an exceptional treatment program for your injuries to help you to begin improving your quality of life immediately.</p>

  <footer class="front__footer">
    <div class="contact contact--area">
      <svg class="icon" width="13" height="13" viewBox="0 0 14 14"><circle cx="7" cy="7" r="6" fill="none" stroke="var(--red)" stroke-width="1.2"/><path d="M7 3.3a2.3 2.3 0 0 0-2.3 2.3C4.7 7.4 7 10.4 7 10.4s2.3-3 2.3-4.8A2.3 2.3 0 0 0 7 3.3z" fill="var(--red)"/><circle cx="7" cy="5.6" r=".9" fill="var(--black)"/></svg>
      <span>Cedar Bend, Hollis Park,<br>Linwood</span>
    </div>
    <div class="contact contact--fax">
      <svg class="icon" width="13" height="13" viewBox="0 0 14 14"><circle cx="7" cy="7" r="6" fill="none" stroke="var(--red)" stroke-width="1.2"/><rect x="3.8" y="5.6" width="6.4" height="4" rx=".6" fill="var(--red)"/><rect x="5" y="3.6" width="4" height="2.2" fill="none" stroke="var(--red)" stroke-width=".8"/></svg>
      <span>(833) 718-2947</span>
    </div>
    <div class="contact contact--phone">
      <svg class="icon" width="13" height="13" viewBox="0 0 14 14"><circle cx="7" cy="7" r="6.5" fill="var(--white)"/><path d="M4.6 3.8l1.4-.3.8 1.8-.9.7a5 5 0 0 0 2.1 2.1l.7-.9 1.8.8-.3 1.4c-3.3.2-5.8-2.3-5.6-5.6z" fill="var(--red)"/></svg>
      <span>(580) 472-6193</span>
    </div>
    <div class="contact contact--web">
      <svg class="icon" width="11" height="11" viewBox="0 0 14 14"><circle cx="7" cy="7" r="6" fill="none" stroke="var(--red)" stroke-width="1.3"/><ellipse cx="7" cy="7" rx="2.4" ry="5" fill="none" stroke="var(--red)"/><path d="M1.5 7h11" stroke="var(--red)"/></svg>
      <span>www.<em>prairieridgerelief</em>.example</span>
    </div>
  </footer>
</section>

<section class="card card--back">
  <div class="card__backdrop"></div>
  <svg class="back__panel" width="320" height="720" viewBox="0 0 320 720">
    <defs>
      <linearGradient id="panelRed" x1="0" y1="0" x2="0" y2="1">
        <stop offset="0" stop-color="#e0151d"/>
        <stop offset="1" stop-color="var(--red-dark)"/>
      </linearGradient>
    </defs>
    <path d="M0,400 C40,440 120,440 160,395 C200,440 280,440 320,380 L320,720 L0,720 Z" fill="url(#panelRed)"/>
  </svg>
  <div class="card__stripes"></div>

  <div class="brand">
    <span class="brand__dot"></span>
    <p class="brand__text">Marsh Medical, LLC dba<br><span class="brand__name">Prairie Ridge Relief Clinic</span><br>Dr. Colin E. Marsh, MD</p>
  </div>

  <svg class="back__gallery" width="320" height="320" viewBox="0 0 320 320">
    <defs>
      <linearGradient id="toneWarm" x1="0" y1="0" x2="1" y2="1"><stop offset="0" stop-color="#a58a72"/><stop offset="1" stop-color="#d8d2c8"/></linearGradient>
      <linearGradient id="toneLight" x1="0" y1="0" x2="1" y2="1"><stop offset="0" stop-color="#f1ede8"/><stop offset="1" stop-color="#cdbfb2"/></linearGradient>
      <linearGradient id="toneStreet" x1="0" y1="0" x2="0" y2="1"><stop offset="0" stop-color="#6b7f99"/><stop offset="1" stop-color="#9a9a9a"/></linearGradient>
      <linearGradient id="toneSoft" x1="0" y1="0" x2="1" y2="1"><stop offset="0" stop-color="#e9e4de"/><stop offset="1" stop-color="#c8b5a6"/></linearGradient>
      <linearGradient id="toneRoom" x1="0" y1="0" x2="1" y2="1"><stop offset="0" stop-color="#6e6c69"/><stop offset="1" stop-color="#e4e0da"/></linearGradient>
    </defs>
    <g stroke="var(--white)" stroke-width="5">
      <circle role="img" aria-label="Photo: older woman who has slipped and fallen on a wet floor" cx="80" cy="87" r="70" fill="url(#toneWarm)"/>
      <circle role="img" aria-label="Photo: woman holding her sore upper back" cx="240" cy="87" r="70" fill="url(#toneLight)"/>
      <circle role="img" aria-label="Photo: woman rubbing her painful shoulder" cx="80" cy="235" r="70" fill="url(#toneSoft)"/>
      <circle role="img" aria-label="Photo: woman with a headache at a table" cx="240" cy="235" r="70" fill="url(#toneRoom)"/>
      <circle role="img" aria-label="Photo: motorcycle accident on a city street" cx="162" cy="162" r="66" fill="url(#toneStreet)"/>
    </g>
  </svg>

  <h2 class="conditions">
    <span class="conditions__kicker">CONDITIONS</span>
    <span class="conditions__title">WE TREAT</span>
  </h2>

  <ul class="conditions__list conditions__list--left">
    <li><svg class="icon" width="9" height="9" viewBox="0 0 10 10"><circle cx="5" cy="5" r="4.3" fill="none" stroke="#fff" stroke-width=".9"/><path d="M3 5.1l1.4 1.4L7 3.8" fill="none" stroke="#fff" stroke-width=".9"/></svg>Car Accident Injuries</li>
    <li><svg class="icon" width="9" height="9" viewBox="0 0 10 10"><circle cx="5" cy="5" r="4.3" fill="none" stroke="#fff" stroke-width=".9"/><path d="M3 5.1l1.4 1.4L7 3.8" fill="none" stroke="#fff" stroke-width=".9"/></svg>Semi Truck Injuries</li>
    <li><svg class="icon" width="9" height="9" viewBox="0 0 10 10"><circle cx="5" cy="5" r="4.3" fill="none" stroke="#fff" stroke-width=".9"/><path d="M3 5.1l1.4 1.4L7 3.8" fill="none" stroke="#fff" stroke-width=".9"/></svg>Most Personal Injuries</li>
    <li><svg class="icon" width="9" height="9" viewBox="0 0 10 10"><circle cx="5" cy="5" r="4.3" fill="none" stroke="#fff" stroke-width=".9"/><path d="M3 5.1l1.4 1.4L7 3.8" fill="none" stroke="#fff" stroke-width=".9"/></svg>Slip and Falls</li>
    <li><svg class="icon" width="9" height="9" viewBox="0 0 10 10"><circle cx="5" cy="5" r="4.3" fill="none" stroke="#fff" stroke-width=".9"/><path d="M3 5.1l1.4 1.4L7 3.8" fill="none" stroke="#fff" stroke-width=".9"/></svg>Motorcycle Accident Injuries</li>
  </ul>
  <ul class="conditions__list conditions__list--right">
    <li><svg class="icon" width="9" height="9" viewBox="0 0 10 10"><circle cx="5" cy="5" r="4.3" fill="none" stroke="#fff" stroke-width=".9"/><path d="M3 5.1l1.4 1.4L7 3.8" fill="none" stroke="#fff" stroke-width=".9"/></svg>Whiplash</li>
    <li><svg class="icon" width="9" height="9" viewBox="0 0 10 10"><circle cx="5" cy="5" r="4.3" fill="none" stroke="#fff" stroke-width=".9"/><path d="M3 5.1l1.4 1.4L7 3.8" fill="none" stroke="#fff" stroke-width=".9"/></svg>Back Injuries</li>
    <li><svg class="icon" width="9" height="9" viewBox="0 0 10 10"><circle cx="5" cy="5" r="4.3" fill="none" stroke="#fff" stroke-width=".9"/><path d="M3 5.1l1.4 1.4L7 3.8" fill="none" stroke="#fff" stroke-width=".9"/></svg>Neck Injuries</li>
    <li><svg class="icon" width="9" height="9" viewBox="0 0 10 10"><circle cx="5" cy="5" r="4.3" fill="none" stroke="#fff" stroke-width=".9"/><path d="M3 5.1l1.4 1.4L7 3.8" fill="none" stroke="#fff" stroke-width=".9"/></svg>Shoulder Injuries</li>
    <li><svg class="icon" width="9" height="9" viewBox="0 0 10 10"><circle cx="5" cy="5" r="4.3" fill="none" stroke="#fff" stroke-width=".9"/><path d="M3 5.1l1.4 1.4L7 3.8" fill="none" stroke="#fff" stroke-width=".9"/></svg>Headaches</li>
  </ul>

  <div class="back__web">
    <svg class="icon" width="10" height="10" viewBox="0 0 14 14"><circle cx="7" cy="7" r="6" fill="none" stroke="#fff" stroke-width="1.2"/><ellipse cx="7" cy="7" rx="2.4" ry="5" fill="none" stroke="#fff"/><path d="M1.5 7h11" stroke="#fff"/></svg>
    <span>www.prairieridgerelief.example</span>
  </div>

  <div class="back__base"></div>
  <svg class="portrait portrait--physician" viewBox="0 0 60 60">
    <circle role="img" aria-label="Portrait of the pain management physician in green scrubs" cx="30" cy="30" r="27.5" fill="#e7ebea" stroke="var(--grey)" stroke-width="4"/>
    <path d="M10,48 C18,38 42,38 50,48 A27 27 0 0 1 10,48Z" fill="#3fa580"/>
  </svg>
  <svg class="portrait portrait--nurse" viewBox="0 0 60 60">
    <circle role="img" aria-label="Portrait of the certified nurse practitioner in a red top" cx="30" cy="30" r="27.5" fill="#ecebea" stroke="var(--grey)" stroke-width="4"/>
    <path d="M10,48 C18,38 42,38 50,48 A27 27 0 0 1 10,48Z" fill="var(--red)"/>
  </svg>
  <p class="staff staff--physician">Colin E. Marsh, M.D.<br>Pain Management Physician</p>
  <p class="staff staff--nurse">Dana Whitfield, APRN-CNP<br>Certified Nurse Practitioner</p>
</section>

</body>
</html>
```